Design einer ITK Unternehmensbroschüre  Grundlayouts mit Deckblatt gesucht
Design einer ITK Unternehmensbroschüre Grundlayouts mit Deckblatt gesucht
Zielgruppe
ITK Systemlösungen mit Schwerpunkt Kommunikationslösungen
Regionale kleine und mittelständische Unternehmen aus allen Branchen
Aufgabenstellung
Vorlage sollte für den Print und Email Versand vorbereitet sein (A4) als Unternehmensbroschüre, die Designlinie sollte bodenständig und innovativ ausgelegt sein.
Dieses Projekt ist als Projektstart zu bewerten und wird in ein eins zu eins Projekt mit erweiterten Budget fortgeführt.
Es soll dazu dienen ein Grundlayout mit Deckblatt zu erstellen um die richtige Linie / Partner zu finden.
Die Kreativität inklusive Aussuchen von passendem Bildmaterial wird vom Designer erwartet und durch Lizenzen im eins zu eins Projekt im Nachgang verrechnet.

```html
<!DOCTYPE html>
<html lang="de">
<head>
<meta charset="utf-8">
<title>Velunix – Unternehmensbroschüre</title>
<link href="https://fonts.googleapis.com/css2?family=PT+Sans:wght@400;700&display=swap" rel="stylesheet">
<style>
:root{
  --brand-blue:#0f3f8f;
  --brand-blue-dark:#0a2c6a;
  --ink:#1f2a44;
  --paper:#ffffff;
  --paper-shade:#e6e7ea;
  --stage:#ffffff;
  --rule:#2c4f95;
}
*{box-sizing:border-box;margin:0;padding:0}
html,body{width:1200px;height:900px;overflow:hidden;background:var(--stage);font-family:"PT Sans",sans-serif;color:var(--ink)}
.canvas{position:relative;width:1200px;height:900px}

/* Cover */
.cover{position:absolute;left:39px;top:204px;width:371px;height:520px;background:linear-gradient(90deg,var(--paper-shade),var(--paper) 30%);box-shadow:2px 4px 10px rgba(0,0,0,.18);overflow:hidden}
.cover-photo{position:absolute;left:0;top:31px;width:371px;height:453px;background:linear-gradient(135deg,#3a4d74 0%,#6f86b4 35%,#a9bbd8 60%,#5a6f98 100%)}
.cover-url{position:absolute;left:16px;top:18px;height:26px;padding:0 10px;background:var(--brand-blue);color:#fff;font-size:14px;line-height:26px;letter-spacing:.2px}
.cover-title-box{position:absolute;left:0;top:274px;width:280px;height:157px;background:var(--brand-blue);color:#fff;display:flex;align-items:center;padding:0 28px}
.cover-title{font-weight:400;font-size:17.5px;line-height:21px}
.cover-brand{position:absolute;left:280px;top:431px;width:91px;height:53px;background:var(--paper);display:flex;align-items:center;justify-content:center;gap:4px}
.brand-name{font-family:"PT Sans",sans-serif;font-weight:700;color:var(--brand-blue);letter-spacing:1px}
.cover-brand .brand-name{font-size:12px}
.brand-dot{width:7px;height:7px;border-radius:50%;background:var(--brand-blue)}
.cover-tagline{position:absolute;left:34px;top:488px;font-size:14px;color:var(--brand-blue);letter-spacing:.6px}

/* Spread */
.spread{position:absolute;left:440px;top:207px;width:724px;height:518px;box-shadow:2px 6px 14px rgba(0,0,0,.2)}
.page{position:absolute;top:0;height:518px;overflow:hidden}
.page-left{left:0;width:362px;background:linear-gradient(160deg,#0b1a3d 0%,#1b4a8e 35%,#163a78 60%,#0a1835 100%)}
.code-visual{position:absolute;inset:0;background:
  radial-gradient(ellipse 90px 18px at 140px 40px,rgba(255,140,60,.55),transparent),
  radial-gradient(ellipse 120px 22px at 150px 330px,rgba(255,110,90,.5),transparent),
  radial-gradient(ellipse 140px 60px at 230px 280px,rgba(80,180,255,.35),transparent),
  radial-gradient(ellipse 60px 200px at 290px 200px,rgba(60,200,255,.2),transparent)}
.page-right{left:362px;width:362px;background:linear-gradient(90deg,#cfd1d6 0%,#f4f4f5 12%,#fbfbfb 60%,#d9dade 100%)}
.band{position:absolute;top:92px;height:89px;background:var(--brand-blue);color:#fff}
.band-left{left:0;width:362px;padding:12px 75px 0 55px;font-size:7px;line-height:9px;text-align:justify}
.band-right{left:362px;width:362px;padding:22px 58px 0 72px;font-size:17px;line-height:21px;text-align:justify}

.page-header{position:absolute;right:6px;top:30px;display:flex;align-items:center;gap:14px}
.page-heading{font-size:18px;color:var(--brand-blue);font-weight:400}
.page-header .brand-name{font-size:11px}

.solutions{position:absolute;left:72px;top:204px;width:231px}
.solution{margin-bottom:10px}
.solution h3{font-size:9.5px;font-weight:400;color:var(--brand-blue);text-align:right;padding-bottom:2px;border-bottom:.6px solid var(--rule);margin-bottom:6px;letter-spacing:.2px}
.solution p{font-size:4.6px;line-height:6.9px;text-align:justify;color:#333}
.solution p+p{margin-top:6px}
.solution-lan{height:92px}
.solution-net{height:64px}
</style>
</head>
<body>
<div class="canvas">

  <section class="cover">
    <div class="cover-photo" role="img" aria-label="Foto: zwei IT-Fachleute im Serverraum vor einer digitalen Netzwerkoberfläche"></div>
    <div class="cover-url">www.velunix-itk.de</div>
    <div class="cover-title-box">
      <h1 class="cover-title">Informationstechnologie- und Telekommunikationslösungen</h1>
    </div>
    <div class="cover-brand"><span class="brand-dot"></span><span class="brand-name">VELUNIX</span></div>
    <p class="cover-tagline">TECHNOLOGISCHE STÄRKEN ERÖFFNEN</p>
  </section>

  <section class="spread">
    <div class="page page-left">
      <div class="code-visual" role="img" aria-label="Foto: unscharfer Programmcode auf einem Bildschirm in Blau und Orange"></div>
    </div>
    <div class="page page-right">
      <header class="page-header">
        <h2 class="page-heading">IT-INFASTRUKTUR</h2>
        <span class="brand-name">VELUNIX</span>
      </header>
      <div class="solutions">
        <article class="solution solution-lan">
          <h3>W-LAN TECHNOLOGIEN</h3>
          <p>Ein stabiles und modernes WLAN Netz setzen Ihre Mitarbeiter, Kunden sowie mögliche IT-Lösungen heutzutage voraus. Zu einer sauberen Einrichtung gehört heutzutage mehr als nur die Einrichtung der Zugangspunkte. Um ein modernes und stabiles WLAN Netz zu gewährleisten, bieten wir Ihnen ein gut durchdachtes Konzept an. Eine Standortbegutachtung gehört für uns im Vorfeld zum Standard, eine Beobachtung der Gegebenheiten wie z.B. äußere Einflüsse, Ausstattung, Gebäudeeigenschaften sowie Funk-Alarmsysteme können das Ergebnis schmälern und zu Problemen führen. Aus diesem Grund bieten wir auch nach Implementierung standardmäßig eine zweite Standortbegutachtung an, um das installierte System im Livebetrieb punktuell zu verbessern. Zusammen mit unseren Technologiepartnern werden wir Ihren Nutzern ein Wohlfühlgefühl auf Ihre Endgeräte zaubern.</p>
        </article>
        <article class="solution solution-net">
          <h3>NETZWERK-INFRASTRUKTUR</h3>
          <p>Wir bieten Ihnen hochverfügbare Routing- und Switching-Lösungen mit leistungsstarken Komponenten und Verkabelungen als Basis. Auch Themen wie Standortvernetzung in Filialstrukturen bringen unser langjähriges KnowHow nicht ins Schwitzen. Mit unseren leistungsstarken Network Monitoring, Network Access Control (NAC) sowie Authentifizierungssystemen und Lösungen monitoren wir auf Wunsch Ihre komplette Netzwerkumgebung.</p>
        </article>
        <article class="solution">
          <h3>LTE-TECHNOLOGIE</h3>
          <p>Trotz des bundesweiten Ausbaus von Glasfasernetzen durch die zahlreichen großen Netzbetreiber sowie kleinen regionalen Carrier, kommt es immer noch vor, dass viele Firmen nicht genügend Bandbreite aufgrund fehlender Infrastrukturversorgung seitens der Carrier zur Verfügung steht. Meistens schlagen die Firmen sich mit teuren symmetrischen Kupfer Stand- oder SDSL-Leitungen mit geringen Bandbreiten für viel Geld rum. Nicht selten investieren die gleichen Firmen in ältere Techniken aufgrund der Bandbreite.</p>
          <p>Wir bieten mit unserer hausinternen LTE Bridge Plus Lösung hohe Bandbreiten im LTE Netz der führenden Carrier und veredeln unsere Lösung mit leistungsstarker Hardware sowie mit ausgefeilter Routingtechnik. So können wir unseren Kunden z.B. trotz LTE eine feste IP-Adresse anbieten, welche es Ihnen ermöglicht auch von außerhalb Ihres Netzwerks auf den Access, bzw. Router zuzugreifen. Unsere Lösung empfiehlt sich vor allem als Backup-Lösung sowie für kleinere Unternehmen, welche mehr Bandbreite benötigen, aber aufgrund der regionalen Infrastruktur keine bekommen.</p>
        </article>
      </div>
    </div>
    <div class="band band-left">Ein Firmennetzwerk ist das Fundament einer jeden Lösung in Ihrem Betrieb. Gerade in Zeiten der Digitalisierung ist es wichtig, sich für die richtige Lösung zu entscheiden und die Grundlage für Ihren technischen Erfolg zu schaffen. Unser KnowHow und langjährige Branchenkontakte ermöglichen es uns, Ihnen die volle Unterstützung bei Planung, Entwicklung, Implementierung sowie dem Betrieb intelligenter Netzwerktechnologien zu gewährleisten</div>
    <div class="band band-right">Folgende Lösungen bieten wir Ihnen an</div>
  </section>

</div>
</body>
</html>
```